Business Card Design

Business card design and logo for new company called TRK Holdings, Inc.
No specific business product line so design would be more focused on the Company name and type style. I would like logo to incorporate Company Lettering "TRK" . Classic example of that would be the Vostin Media logo. Intent that the "TRK" lettering design would also be the Company Logo design.
Note that contact information for business card does not have telephone / fax numbers and web site as that will follow but make allowance for that information in the business card design. Several of the design layouts has small logo instead of the wording for phone, fax ..... which I would prefer.
Target Market(s)
Small Businesses
Industry/Entity Type
Business
Contact Information for Business Card
Lionel Pratt
TRK Holdings, Inc.
48620 Marrow Lane, Unit F
Harlow Vale, NV 90527
Phone: 555.218.6034
Mobile: 555.730.1946
FAX: 555.730.5287
Email: lpratt@trkholdings.example
Web: www.trkholdings.example
Font styles to use
Other font styles liked:
- Helvetica
Look and feel

```html
<!DOCTYPE html>
<html lang="en">
<head>
<meta charset="utf-8">
<title>TRK Holdings, Inc. – Business Card</title>
<link rel="stylesheet" href="https://fonts.googleapis.com/css2?family=Arimo:wght@400&display=swap">
<style>
  :root {
    --card-bg: #1a1f1f;
    --brand-green: #3fc190;
    --text-green: #3fb487;
    --band-light: #55917b;
    --band-dark: #3b6b5b;
  }
  html, body {
    margin: 0;
    padding: 0;
    overflow: hidden;
    background: var(--card-bg);
  }
  .card {
    position: relative;
    width: 1200px;
    height: 702px;
    background: var(--card-bg);
    overflow: hidden;
    font-family: "Arimo", Helvetica, Arial, sans-serif;
    color: var(--text-green);
  }
  .wave-band {
    position: absolute;
    inset: 0;
    width: 1200px;
    height: 702px;
  }
  .company-name {
    position: absolute;
    left: 75px;
    top: 92px;
    margin: 0;
    font-size: 76px;
    font-weight: 400;
    line-height: 1;
    letter-spacing: -0.5px;
    color: var(--brand-green);
    white-space: nowrap;
  }
  .contact {
    position: absolute;
    left: 75px;
    margin: 0;
    font-size: 18px;
    line-height: 1;
    white-space: nowrap;
  }
  .address-line-1 { top: 194px; }
  .address-line-2 { top: 218px; }
  .phone  { top: 260px; }
  .mobile { top: 287px; }
  .fax    { top: 313px; font-size: 21px; }
  .email  { top: 345px; }
  .person-name {
    position: absolute;
    right: 85px;
    top: 566px;
    margin: 0;
    font-size: 34px;
    font-weight: 400;
    line-height: 1;
    white-space: nowrap;
  }
  .website {
    position: absolute;
    right: 85px;
    top: 602px;
    margin: 0;
    font-size: 24px;
    line-height: 1;
    white-space: nowrap;
  }
</style>
</head>
<body>
  <main class="card">
    <svg class="wave-band" viewBox="0 0 1200 702" role="img" aria-label="Decorative wave of tilted green blocks sweeping across the card">
      <defs>
        <linearGradient id="band-fill" x1="0" y1="0" x2="1" y2="0">
          <stop offset="0" stop-color="var(--band-dark)"/>
          <stop offset="0.5" stop-color="var(--band-light)"/>
          <stop offset="1" stop-color="var(--band-dark)"/>
        </linearGradient>
      </defs>
      <path fill="url(#band-fill)"
        d="M0,345 C150,430 260,440 400,420 C600,385 700,270 850,215 C1000,170 1100,165 1200,170
           L1200,345 C1050,345 950,385 820,455 C650,545 520,575 380,610 C230,645 100,580 0,520 Z"/>
    </svg>

    <h1 class="company-name">TRK Holdings, Inc.</h1>

    <p class="contact address-line-1">48620 Marrow Lane</p>
    <p class="contact address-line-2">Unit F Harlow Vale, NV 90527</p>
    <p class="contact phone">Phone: 555.218.6034</p>
    <p class="contact mobile">Mobile: 555.730.1946</p>
    <p class="contact fax">FAX: 555.730.5287</p>
    <p class="contact email">Email: lpratt@trkholdings.example</p>

    <h2 class="person-name">Lionel Pratt</h2>
    <p class="website">Web: www.trkholdings.example</p>
  </main>
</body>
</html>
```